Varlow's Electrical & Solar - Business Cards

I want my business card to stand out from the rest. I will provide my business name logo and my icon logo to be implemented onto the card.

On the front of the card, can i have the following. Just make it neat & professional please.

Dean Harrop
varlowselectrical@mailbox-example.net
0491 837 562
ABN: 41 269 507 813
License No. 582146K
FREE QUOTES
24/7 Emergency

On the back of the card, can I have "Our Services" and maybe add the V logo on the back in the background or something. Under "Our Services" I want the following:

LED Lighting Upgrades
Switches & Outlets
Smoke Alarms
Switchboard Upgrades
Fault Finding
Rewiring
New Builds
Test & Tagging
All Electrical Maintenance & Repairs

Can you guys add the instagram logo and next to it, put varlows_electrical

Can you guys also add the facebook logo and next to it put Varlow's Electrical & Solar. Make sure the instagram & facebook icon is in either white, green or black.

Also I have put down double sided, not sure why when i save it, it keeps going to single sided. I need my business card double sided.

New Customers

Dean Harrop varlowselectrical@mailbox-example.net 0491 837 562 ABN: 41 269 507 813 License No. 582146K FREE QUOTES 24/7 Emergency

• must be tidy, professional and appealing

```html
<!DOCTYPE html>
<html lang="en">
<head>
<meta charset="utf-8">
<title>Varlow's Electrical &amp; Solar – Business Cards</title>
<link href="https://fonts.googleapis.com/css2?family=Russo+One&family=Lato:wght@400;700&display=swap" rel="stylesheet">
<style>
  :root {
    --bg: #2a2a2a;
    --card: #1b1b1c;
    --card-edge: #242425;
    --green: #22b43a;
    --green-bright: #3fd24f;
    --silver: #c9cbce;
    --white: #f2f2f2;
    --muted: #3a3a3c;
  }
  * { box-sizing: border-box; margin: 0; padding: 0; }
  html, body { width: 1200px; height: 875px; overflow: hidden; }
  body {
    background: var(--bg);
    font-family: "Lato", sans-serif;
    color: var(--white);
    position: relative;
  }
  .card {
    position: absolute;
    width: 560px;
    height: 320px;
    background: var(--card);
    border-radius: 18px;
    overflow: hidden;
    box-shadow: 0 18px 40px rgba(0,0,0,.45);
  }

  /* ---------- back ---------- */
  .card-back { left: 50px; top: 100px; }
  .back-mark {
    position: absolute;
    left: 24px; top: 90px;
    width: 250px; height: 200px;
    display: flex; align-items: center; justify-content: center;
    font-family: "Russo One", sans-serif;
    font-size: 58px;
    color: #3b3b3d;
  }
  .services-banner {
    position: absolute;
    right: 0; top: 26px;
    width: 300px; height: 46px;
    background: var(--green);
    clip-path: polygon(22px 0, 100% 0, 100% 100%, 0 100%);
    display: flex; align-items: center; justify-content: center;
    font-family: "Russo One", sans-serif;
    font-size: 25px;
    color: #0f0f0f;
    letter-spacing: 1px;
  }
  .services-list {
    position: absolute;
    right: 26px; top: 88px;
    list-style: none;
    text-align: right;
    font-size: 16px;
    line-height: 21px;
  }
  .services-list li { display: flex; justify-content: flex-end; align-items: flex-start; gap: 10px; }
  .services-list .tick { width: 13px; height: 13px; margin-top: 4px; flex: none; }
  .services-list .no-tick { width: 13px; flex: none; }

  /* ---------- front ---------- */
  .card-front { left: 590px; top: 455px; }
  .brand {
    position: absolute;
    left: 70px; top: 26px;
    display: flex; align-items: center; gap: 14px;
  }
  .brand-dot {
    width: 54px; height: 54px; border-radius: 50%;
    border: 4px solid var(--green);
  }
  .brand-name {
    font-family: "Russo One", sans-serif;
    font-size: 50px;
    color: var(--silver);
    line-height: 1;
  }
  .brand-sub {
    position: absolute;
    left: 138px; top: 84px;
    font-family: "Russo One", sans-serif;
    font-size: 12px;
    letter-spacing: 5px;
    color: var(--silver);
  }
  .holder-name {
    position: absolute;
    left: 34px; top: 128px;
    font-family: "Russo One", sans-serif;
    font-size: 30px;
    color: var(--green);
  }
  .divider {
    position: absolute;
    left: 34px; right: 34px; top: 170px;
    height: 2px; background: #8a8a8c;
  }
  .contact { position: absolute; left: 34px; top: 182px; font-size: 15px; }
  .contact-row { display: flex; align-items: center; gap: 9px; margin-bottom: 3px; }
  .contact-row.phone { font-size: 20px; }
  .contact-row svg { width: 14px; height: 14px; flex: none; }
  .free-quotes {
    position: absolute; left: 34px; top: 250px;
    font-weight: 700; font-size: 19px;
  }
  .free-quotes .accent { color: var(--green); }
  .legal {
    position: absolute; left: 320px; top: 182px;
    font-size: 15px; line-height: 21px;
  }
  .legal .label { color: var(--green); font-weight: 700; }
  .emergency {
    position: absolute; right: 28px; top: 110px;
    display: flex; align-items: center;
  }
  .emergency-tag {
    background: var(--green);
    color: #0f0f0f;
    font-weight: 700; font-size: 10px; line-height: 11px;
    padding: 3px 8px 3px 10px; margin-left: -8px;
    clip-path: polygon(0 0, 88% 0, 100% 50%, 88% 100%, 0 100%);
  }
  .bottom-band {
    position: absolute; left: 0; bottom: 0;
    width: 100%; height: 14px;
    background: var(--green);
  }
  .social-tab {
    position: absolute; right: 0; bottom: 14px;
    width: 250px; height: 40px;
    background: var(--silver);
    clip-path: polygon(14px 0, 100% 0, 100% 100%, 0 100%);
    display: flex; align-items: center; justify-content: center; gap: 7px;
    color: #111; font-size: 16px;
  }
  .social-dot { width: 16px; height: 16px; border-radius: 50%; background: #111; }
  .social-handle { margin-left: 5px; }
</style>
</head>
<body>

<section class="card card-back" aria-label="Business card back">
  <div class="back-mark">VARLOW'S</div>
  <div class="services-banner">OUR SERVICES</div>
  <ul class="services-list">
    <li>LED Lighting Upgrades<svg class="tick" viewBox="0 0 14 14"><circle cx="7" cy="7" r="7" fill="#22b43a"/><path d="M3.8 7.2l2.2 2.2 4.2-4.4" stroke="#111" stroke-width="1.8" fill="none"/></svg></li>
    <li>Switches &amp; Outlets<svg class="tick" viewBox="0 0 14 14"><circle cx="7" cy="7" r="7" fill="#22b43a"/><path d="M3.8 7.2l2.2 2.2 4.2-4.4" stroke="#111" stroke-width="1.8" fill="none"/></svg></li>
    <li>Smoke Alarms<svg class="tick" viewBox="0 0 14 14"><circle cx="7" cy="7" r="7" fill="#22b43a"/><path d="M3.8 7.2l2.2 2.2 4.2-4.4" stroke="#111" stroke-width="1.8" fill="none"/></svg></li>
    <li>Fault Finding<svg class="tick" viewBox="0 0 14 14"><circle cx="7" cy="7" r="7" fill="#22b43a"/><path d="M3.8 7.2l2.2 2.2 4.2-4.4" stroke="#111" stroke-width="1.8" fill="none"/></svg></li>
    <li>Rewiring<svg class="tick" viewBox="0 0 14 14"><circle cx="7" cy="7" r="7" fill="#22b43a"/><path d="M3.8 7.2l2.2 2.2 4.2-4.4" stroke="#111" stroke-width="1.8" fill="none"/></svg></li>
    <li>Switchboard Upgrades<svg class="tick" viewBox="0 0 14 14"><circle cx="7" cy="7" r="7" fill="#22b43a"/><path d="M3.8 7.2l2.2 2.2 4.2-4.4" stroke="#111" stroke-width="1.8" fill="none"/></svg></li>
    <li>New Builds<svg class="tick" viewBox="0 0 14 14"><circle cx="7" cy="7" r="7" fill="#22b43a"/><path d="M3.8 7.2l2.2 2.2 4.2-4.4" stroke="#111" stroke-width="1.8" fill="none"/></svg></li>
    <li>Test &amp; Tagging<svg class="tick" viewBox="0 0 14 14"><circle cx="7" cy="7" r="7" fill="#22b43a"/><path d="M3.8 7.2l2.2 2.2 4.2-4.4" stroke="#111" stroke-width="1.8" fill="none"/></svg></li>
    <li>All Electrical Maintenance<svg class="tick" viewBox="0 0 14 14"><circle cx="7" cy="7" r="7" fill="#22b43a"/><path d="M3.8 7.2l2.2 2.2 4.2-4.4" stroke="#111" stroke-width="1.8" fill="none"/></svg></li>
    <li>&amp; Repairs<span class="no-tick"></span></li>
  </ul>
</section>

<section class="card card-front" aria-label="Business card front">
  <div class="brand">
    <span class="brand-dot"></span>
    <span class="brand-name">VARLOW'S</span>
  </div>
  <div class="brand-sub">ELECTRICAL &amp; SOLAR</div>

  <div class="emergency">
    <svg width="34" height="34" viewBox="0 0 34 34" aria-hidden="true"><circle cx="17" cy="17" r="14" fill="none" stroke="#22b43a" stroke-width="3"/><path d="M17 9v8h6" stroke="#22b43a" stroke-width="2.5" fill="none"/></svg>
    <span class="emergency-tag">24/7<br>EMERGENCY</span>
  </div>

  <div class="holder-name">DEAN HARROP</div>
  <div class="divider"></div>

  <div class="contact">
    <div class="contact-row phone">
      <svg viewBox="0 0 14 14" aria-hidden="true"><path d="M3 1.5l2.2 2.6-1.2 1.6a8 8 0 0 0 4.3 4.3l1.6-1.2 2.6 2.2-1.3 1.6C6.6 12.8 1.2 7.4 1.4 2.8z" fill="#22b43a"/></svg>
      <span>0491 837 562</span>
    </div>
    <div class="contact-row">
      <svg viewBox="0 0 14 14" aria-hidden="true"><rect x="1" y="3" width="12" height="8.5" rx="1" fill="#22b43a"/><path d="M1.5 3.5L7 8l5.5-4.5" stroke="#111" stroke-width="1.2" fill="none"/></svg>
      <span>varlowselectrical@mailbox-example.net</span>
    </div>
  </div>

  <div class="legal">
    <div><span class="label">ABN:</span> 41 269 507 813</div>
    <div><span class="label">Lic No.</span> 582146K</div>
  </div>

  <div class="free-quotes"><span class="accent">FREE</span> QUOTES</div>

  <div class="social-tab">
    <span class="social-dot"></span>
    <span class="social-dot"></span>
    <span class="social-handle">varlows_electrical</span>
  </div>
  <div class="bottom-band"></div>
</section>

</body>
</html>
```